agricultural technology company needs business cards*

design a business card that represents our business well. please see our website: vastrelbyfieldseal.com.au
professional, simple, clean lines, not complicated or floral.....

```html
<!DOCTYPE html>
<html lang="en">
<head>
<meta charset="utf-8">
<title>Vastrelby Fieldseal – Business Cards</title>
<link href="https://fonts.googleapis.com/css2?family=Roboto:wght@400;500;900&display=swap" rel="stylesheet">
<style>
  :root {
    --green: #2bb04a;
    --lime: #a3c93a;
    --navy: #1c2f5a;
    --white: #ffffff;
    --stage: #3b3b3d;
    --rule: #3a4660;
  }
  * { box-sizing: border-box; margin: 0; padding: 0; }
  html, body {
    width: 1200px; height: 901px; overflow: hidden;
    background: var(--stage);
    font-family: "Roboto", Arial, sans-serif;
  }
  .card {
    position: absolute;
    width: 620px; height: 354px;
    overflow: hidden;
  }
  /* Front side */
  .card-front {
    left: 70px; top: 80px;
    background: var(--green);
    color: var(--white);
  }
  .card-front .wordmark {
    position: absolute; right: 44px; top: 150px;
    text-align: right;
    font-weight: 900; font-size: 46px; line-height: 0.95;
    letter-spacing: -0.5px;
  }
  .card-front .web {
    position: absolute; right: 44px; top: 262px;
    font-size: 17px; font-weight: 400; letter-spacing: 0.3px;
  }
  /* Back side */
  .card-back {
    left: 510px; top: 450px;
    background: var(--white);
  }
  .brand {
    position: absolute; left: 40px; top: 148px;
    display: flex; align-items: center; gap: 12px;
  }
  .brand-square { width: 22px; height: 22px; background: var(--green); }
  .brand-name {
    font-weight: 900; font-size: 30px; line-height: 0.95;
    color: var(--navy); letter-spacing: -0.4px;
  }
  .divider {
    position: absolute; left: 292px; top: 60px;
    width: 1px; height: 170px; background: var(--rule);
  }
  .contact {
    position: absolute; left: 312px; top: 58px;
    color: var(--navy); font-size: 13px; line-height: 1.3;
  }
  .contact .person { color: var(--green); font-weight: 500; font-size: 19px; }
  .contact .role { font-size: 14px; margin-bottom: 12px; }
  .contact .address { margin-bottom: 12px; }
  .contact ul { list-style: none; }
  .contact li { display: flex; align-items: center; gap: 8px; margin-bottom: 3px; }
  .contact li svg { width: 12px; height: 12px; flex: none; }
  .contact .accent { color: var(--green); }
  .card-back .bands { position: absolute; left: 0; bottom: 0; width: 620px; height: 80px; }
</style>
</head>
<body>

<section class="card card-front" aria-label="Card front">
  <div class="wordmark">Vastrelby<br>Fieldseal</div>
  <div class="web">www.vastrelbyfieldseal.com.au</div>
</section>

<section class="card card-back" aria-label="Card back">
  <div class="brand">
    <span class="brand-square"></span>
    <span class="brand-name">Vastrelby<br>Fieldseal</span>
  </div>

  <div class="divider"></div>

  <div class="contact">
    <div class="person">Marcus Hale</div>
    <div class="role">Manager</div>
    <div class="address">52 Harlow Street,<br>Kelmscott, WA 6111</div>
    <ul>
      <li>
        <svg viewBox="0 0 24 24" fill="var(--green)"><path d="M6.6 10.8a15 15 0 0 0 6.6 6.6l2.2-2.2a1 1 0 0 1 1-.25 11 11 0 0 0 3.6.6 1 1 0 0 1 1 1V20a1 1 0 0 1-1 1A17 17 0 0 1 3 4a1 1 0 0 1 1-1h3.5a1 1 0 0 1 1 1c0 1.25.2 2.45.6 3.6a1 1 0 0 1-.25 1z"/></svg>
        1300 482 613
      </li>
      <li>
        <svg viewBox="0 0 24 24" fill="none" stroke="var(--green)" stroke-width="2.4"><rect x="3" y="5" width="18" height="14"/><path d="M3 5l9 8 9-8"/></svg>
        hello@vastrelbyfieldseal.com.au
      </li>
      <li>
        <svg viewBox="0 0 24 24" fill="none" stroke="var(--green)" stroke-width="2"><circle cx="12" cy="12" r="9"/><path d="M3 12h18M12 3c3 3 3 15 0 18M12 3c-3 3-3 15 0 18"/></svg>
        <span>www.<span class="accent">vastrelbyfieldseal</span>.com.au</span>
      </li>
    </ul>
  </div>

  <svg class="bands" viewBox="0 0 620 80" aria-hidden="true">
    <polygon points="0,80 0,66 380,54 376,80" fill="var(--lime)"/>
    <polygon points="388,80 392,52 620,44 620,80" fill="var(--green)"/>
  </svg>
</section>

</body>
</html>
```